Project Title:
Dental Implant Overdenture Flyer (Retirement Village Target)
Objective:
Create a clean, trustworthy, and reassuring flyer aimed at older adults (60–85 years old) who struggle with loose dentures. The goal is to educate them about implant-retained “clip-on” dentures and encourage them to book a consultation.
Tone & Feel:
Warm, caring, non-intimidating
Premium but not “salesy”
Medical but easy to understand
Focus on improving quality of life (confidence, eating, comfort)
Target Audience:
Retirees / pensioners
Existing denture wearers
People frustrated with loose or uncomfortable dentures
Key Message:
“You don’t have to live with loose dentures anymore.”
Design Style:
Clean, minimal, modern
Soft colours (blues, greens, warm neutrals)
Easy-to-read large font
High contrast for older eyes
Avoid clutter
Imagery Suggestions:
Smiling older adults (natural, not stocky/overly staged)
Before/after lifestyle (eating, laughing, socialising)
Simple diagram showing denture clipping onto implants
Avoid graphic surgical images
Layout Suggestions:
A5 or DL flyer
Clear sections with headings
Icons for benefits
Strong call-to-action at bottom
HEADLINE (big and bold)
Tired of Loose Dentures?
Discover Secure “Clip-On” Teeth
🔹 PROBLEM SECTION
Do your dentures:
Slip or move when eating?
Make it hard to chew certain foods?
Feel uncomfortable or loose?
Affect your confidence when speaking or smiling?
You’re not alone — and there is a better solution.
🔹 SOLUTION SECTION
Implant-Retained “Clip-On” Dentures
We can secure your denture using just 2 dental implants, allowing your teeth to:
✔ Stay firmly in place
✔ Improve your ability to eat
✔ Feel more comfortable
✔ Boost your confidence
🔹 SIMPLE EXPLANATION (very important)
Small titanium implants are gently placed in the jaw.
Your denture then clips securely onto them, stopping movement.
🔹 PRICE SECTION (highlight this clearly)
$12,000
Includes:
2 dental implants
A brand new custom overdenture
Does not include sedation or extractions (if needed)
🔹 SEDATION
Sedation is available for comfort.
If you hold a pensioner card, you may receive a significant Vantacor rebate, often resulting in minimal out-of-pocket costs for sedation.
🔹 TRUST / REASSURANCE
Experienced implant clinician
Gentle, patient-focused care
Modern technology and techniques
🔹 CALL TO ACTION (VERY IMPORTANT)
Book a Free Consultation
📞 Call: 08 9351 4276
🌐 Visit: www.bravonclinic.com.au
📍 Located near Tallowmere shopping centre
🔹 OPTIONAL TAGLINE
Eat Better. Feel Better. Smile with Confidence Again.
Please include some photos to illustrate what a clip on denture looks like with two implants.

```html
<!DOCTYPE html>
<html lang="en">
<head>
<meta charset="UTF-8">
<title>Clip-On Denture Flyer</title>
<link href="https://fonts.googleapis.com/css2?family=Montserrat:wght@400;500;600;700&display=swap" rel="stylesheet">
<style>
  :root {
    --teal-light: #4cc1bc;
    --teal-dark: #1d93ae;
    --brand: #1f8fa6;
    --ink: #1a1a1a;
    --white: #ffffff;
    --stage: #e9e9e9;
    --photo-a: #e6f1f8;
    --photo-b: #a9cde6;
  }
  * { box-sizing: border-box; margin: 0; padding: 0; }
  html, body { width: 1200px; height: 1200px; overflow: hidden; }
  body {
    background: var(--stage);
    font-family: "Montserrat", sans-serif;
    position: relative;
  }
  .panel {
    position: absolute;
    top: 65px;
    width: 506px;
    height: 1070px;
    background: var(--white);
    overflow: hidden;
  }
  .panel--front { left: 71px; }
  .panel--back { left: 624px; }
  .panel__shapes { position: absolute; inset: 0; }

  .brand {
    position: absolute;
    top: 100px;
    left: 0;
    width: 100%;
    display: flex;
    align-items: center;
    justify-content: center;
    gap: 16px;
    color: var(--brand);
    font-weight: 600;
  }
  .brand__dot {
    width: 54px; height: 54px;
    border-radius: 50%;
    background: var(--teal-light);
  }
  .brand__name { font-size: 30px; letter-spacing: 5px; line-height: 1.1; }
  .brand__name span { display: block; font-size: 20px; letter-spacing: 1.5px; }

  .text { position: absolute; left: 0; width: 100%; text-align: center; color: var(--white); }
  .text--dark { color: var(--ink); }

  .headline { top: 327px; font-size: 38px; font-weight: 700; line-height: 38px; }
  .subhead { top: 410px; font-size: 22px; font-weight: 600; line-height: 28px; }

  .problem__title { top: 526px; font-size: 20px; font-weight: 700; line-height: 26px; }
  .problem__list { top: 573px; font-size: 18px; line-height: 22px; list-style: none; }
  .problem__close { top: 686px; font-size: 18px; line-height: 23px; }

  .solution {
    position: absolute; top: 868px; left: 70px; right: 20px;
    color: var(--white); font-size: 17.5px; line-height: 22px;
  }
  .solution__list { list-style: none; margin-top: 21px; }
  .solution__list li { display: flex; align-items: center; gap: 5px; line-height: 21.7px; }
  .tick { width: 11px; height: 11px; flex: none; }

  .explain { top: 256px; font-size: 17.5px; line-height: 22px; }
  .price__amount { top: 444px; font-size: 58px; font-weight: 700; line-height: 60px; }
  .price__includes { top: 498px; font-size: 17.5px; line-height: 21px; }
  .price__sedation { top: 574px; font-size: 17.5px; line-height: 22px; }

  .photo {
    position: absolute; top: 620px; left: 0; width: 100%; height: 152px;
    background: linear-gradient(90deg, var(--photo-a), var(--photo-b) 70%, var(--photo-a));
  }
  .trust { top: 793px; font-size: 17.5px; line-height: 22.5px; }
  .cta__title { top: 922px; font-size: 17.5px; font-weight: 700; line-height: 24px; }
  .cta__details { top: 965px; font-size: 17.5px; line-height: 22px; }
</style>
</head>
<body>

  <section class="panel panel--front">
    <svg class="panel__shapes" viewBox="0 0 506 1070" width="506" height="1070" aria-hidden="true">
      <circle cx="251" cy="501" r="256" fill="var(--teal-light)"/>
      <path d="M0 579 Q140 490 300 500 Q430 510 506 540 L506 1070 L0 1070 Z" fill="var(--teal-dark)"/>
      <path d="M0 847 Q180 740 506 770 L506 1070 L0 1070 Z" fill="var(--white)"/>
      <path d="M0 860 Q185 755 506 783 L506 1070 L0 1070 Z" fill="var(--teal-light)"/>
    </svg>

    <div class="brand">
      <div class="brand__dot"></div>
      <div class="brand__name">BRAVON<span>DENTAL SURGERY</span></div>
    </div>

    <h1 class="text headline">TIRED OF LOOSE<br>DENTURES?</h1>
    <p class="text subhead">Discover Secure “Clip-On” Teeth</p>

    <h2 class="text problem__title">Do your dentures:</h2>
    <ul class="text problem__list">
      <li>Slip or move when eating?</li>
      <li>Make it hard to chew certain foods?</li>
      <li>Feel uncomfortable or loose?</li>
      <li>Affect your confidence when speaking or smiling?</li>
    </ul>
    <p class="text problem__close">You’re not alone — and there is a better solution.<br>Implant-Retained “Clip-On” Dentures</p>

    <div class="solution">
      <p>We can secure your denture using just 2<br>dental implants, allowing your teeth to:</p>
      <ul class="solution__list">
        <li><svg class="tick" viewBox="0 0 10 10"><path d="M1 5 L4 8 L9 2" stroke="var(--white)" stroke-width="2" fill="none"/></svg>Stay firmly in place</li>
        <li><svg class="tick" viewBox="0 0 10 10"><path d="M1 5 L4 8 L9 2" stroke="var(--white)" stroke-width="2" fill="none"/></svg>Improve your ability to eat</li>
        <li><svg class="tick" viewBox="0 0 10 10"><path d="M1 5 L4 8 L9 2" stroke="var(--white)" stroke-width="2" fill="none"/></svg>Feel more comfortable</li>
        <li><svg class="tick" viewBox="0 0 10 10"><path d="M1 5 L4 8 L9 2" stroke="var(--white)" stroke-width="2" fill="none"/></svg>Boost your confidence</li>
      </ul>
    </div>
  </section>

  <section class="panel panel--back">
    <svg class="panel__shapes" viewBox="0 0 506 1070" width="506" height="1070" aria-hidden="true">
      <circle cx="254" cy="577" r="207" fill="var(--teal-dark)"/>
      <circle cx="254" cy="1130" r="255" fill="var(--teal-light)"/>
    </svg>

    <div class="brand">
      <div class="brand__dot"></div>
      <div class="brand__name">BRAVON<span>DENTAL SURGERY</span></div>
    </div>

    <p class="text text--dark explain">Small titanium implants are gently<br>placed in the jaw.<br>Your denture then clips securely onto<br>them, stopping movement.</p>

    <p class="text price__amount">$12,000</p>
    <p class="text price__includes">2 dental implants<br>A brand new custom overdenture</p>
    <p class="text price__sedation">Sedation is available for comfort.</p>

    <div class="photo" role="img" aria-label="Photo of a tooth model with dental mirror and probe in a bright dental clinic"></div>

    <p class="text text--dark trust">Experienced implant clinician<br>Gentle, patient-focused care<br>Modern technology and techniques</p>

    <h2 class="text cta__title">Book a Free Consultation</h2>
    <p class="text cta__details">08 9351 4276<br>www.bravonclinic.com.au<br>Located near Tallowmere shopping centre</p>
  </section>

</body>
</html>
```